Pinegate Mobile Imaging
Mobile ultrasound business cards
Danelle Forbush RDMS, RVT, RT(R)
Owner
418 Whitford Ave. Ste 203-117 Bowling Green, KY 42104
leave space to add later
danelle_forbush2006@mailbright.net
There is also a second owner that once design is finalized we will need to edit the text to put her information on the card.
email used on card will need to be changed at a later date!

```html
<!DOCTYPE html>
<html lang="en">
<head>
<meta charset="utf-8">
<title>Pinegate Mobile Imaging — Stationery</title>
<link rel="stylesheet" href="https://fonts.googleapis.com/css2?family=Open+Sans:wght@400;600&display=swap">
<style>
  :root {
    --bg: #e6e4ea;
    --paper: #ffffff;
    --purple: #6e2a86;
    --violet: #9b59b6;
    --lilac-soft: #efe6f4;
    --ink: #4a4150;
    --muted: #8a8290;
  }
  * { box-sizing: border-box; margin: 0; padding: 0; }
  html, body { width: 1200px; height: 679px; overflow: hidden; }
  body {
    background: var(--bg);
    font-family: "Open Sans", Arial, sans-serif;
    color: var(--ink);
    position: relative;
  }
  .sheet { position: absolute; background: var(--paper); box-shadow: 0 6px 18px rgba(40,20,50,.18); overflow: hidden; }

  .brand-name {
    font-family: "Open Sans", Arial, sans-serif;
    font-weight: 600;
    color: var(--purple);
    line-height: 1.2;
    white-space: nowrap;
  }

  .base-band { position: absolute; left: 0; right: 0; bottom: 0; background: repeating-linear-gradient(90deg, var(--purple) 0 3px, var(--violet) 3px 6px); }

  /* Letterhead */
  .letterhead { left: 60px; top: 90px; width: 360px; height: 500px; }
  .letterhead .brand-name { position: absolute; left: 26px; top: 28px; font-size: 13px; }
  .letterhead .sender { position: absolute; right: 26px; top: 30px; text-align: right; font-size: 6.5px; line-height: 1.55; color: var(--muted); }
  .letterhead .base-band { height: 8px; }

  /* Envelope */
  .envelope { left: 470px; top: 70px; width: 460px; height: 220px; }
  .envelope .brand-name { position: absolute; left: 22px; top: 22px; font-size: 12px; }
  .envelope .return { position: absolute; left: 22px; top: 42px; font-size: 6.5px; line-height: 1.5; color: var(--muted); }
  .envelope .base-band { height: 6px; }

  /* Business cards */
  .card { width: 300px; height: 172px; top: 340px; border-radius: 4px; }
  .card .base-band { height: 10px; }
  .card-front { left: 470px; }
  .card-front .brand-name { position: absolute; left: 20px; top: 20px; font-size: 12px; }
  .card-front .holder { position: absolute; left: 20px; top: 60px; }
  .holder-name { font-size: 12px; font-weight: 600; color: var(--purple); }
  .holder-creds { font-size: 8px; color: var(--muted); }
  .holder-role { font-size: 8.5px; margin-top: 2px; }
  .card-front .contact { position: absolute; right: 18px; bottom: 22px; text-align: right; font-size: 7.5px; line-height: 1.55; }
  .card-front .contact .space { color: var(--muted); }

  .card-back { left: 800px; background: linear-gradient(160deg, var(--paper) 40%, var(--lilac-soft) 100%); }
  .card-back .brand-name { position: absolute; width: 100%; top: 62px; text-align: center; font-size: 17px; }
  .card-back .web { position: absolute; width: 100%; top: 104px; text-align: center; font-size: 9px; color: var(--purple); font-weight: 600; }
</style>
</head>
<body>

<section class="sheet letterhead">
  <p class="brand-name">Pinegate Mobile Imaging</p>
  <address class="sender">
    418 Whitford Ave. Ste 203-117<br>
    Bowling Green, KY 42104<br>
    Phone 270-555-0148<br>
    danelle_forbush2006@mailbright.net
  </address>
  <div class="base-band"></div>
</section>

<section class="sheet envelope">
  <p class="brand-name">Pinegate Mobile Imaging</p>
  <address class="return">
    418 Whitford Ave. Ste 203-117<br>
    Bowling Green, KY 42104
  </address>
  <div class="base-band"></div>
</section>

<section class="sheet card card-front">
  <p class="brand-name">Pinegate Mobile Imaging</p>
  <div class="holder">
    <p class="holder-name">Danelle Forbush</p>
    <p class="holder-creds">RDMS, RVT, RT(R)</p>
    <p class="holder-role">Owner</p>
  </div>
  <address class="contact">
    418 Whitford Ave. Ste 203-117<br>
    Bowling Green, KY 42104<br>
    <span class="space">Phone 270-555-0148</span><br>
    danelle_forbush2006@mailbright.net
  </address>
  <div class="base-band"></div>
</section>

<section class="sheet card card-back">
  <p class="brand-name">Pinegate Mobile Imaging</p>
  <p class="web">www.pinegatemobileimaging.com</p>
  <div class="base-band"></div>
</section>

</body>
</html>
```